Residential Remodeling Contractor needs updated business card

I need a new design for my business card.
Name of the company is Brookfell Construction. I need a card that commands presence, strength, integrity. I have been in business for 28 years. I am a Residential Remodeling Contractor that covers all aspects of a residential remodel and build.

```html
<!DOCTYPE html>
<html lang="en">
<head>
<meta charset="utf-8">
<title>Brookfell Construction – Business Card</title>
<link rel="stylesheet" href="https://fonts.googleapis.com/css2?family=Libre+Baskerville:wght@700&family=Arimo:wght@400&display=swap">
<style>
  :root {
    --page-bg: #e9e9ec;
    --card-blue: #1a3f7e;
    --card-blue-deep: #1d3a78;
    --emboss-blue: #22407f;
    --ink-white: #ffffff;
    --shadow: rgba(10, 20, 50, 0.25);
  }
  * { box-sizing: border-box; margin: 0; padding: 0; }
  html, body {
    width: 1200px; height: 912px; overflow: hidden;
    background: var(--page-bg);
  }
  .sheet {
    position: relative; width: 1200px; height: 912px;
  }
  .card {
    position: absolute; left: 240px; width: 720px; height: 410px;
    border-radius: 22px; overflow: hidden;
    box-shadow: 0 10px 28px var(--shadow);
  }
  .card--front { top: 30px; background: var(--card-blue-deep); }
  .card--back { top: 472px; background: var(--card-blue); }

  .wordmark {
    font-family: "Libre Baskerville", Georgia, serif;
    font-weight: 700; text-transform: uppercase; line-height: 1.05;
    white-space: nowrap;
  }
  .card--front .wordmark {
    position: absolute; left: 175px; top: 140px;
    color: var(--emboss-blue); font-size: 44px; letter-spacing: 1px;
  }
  .card--front .wordmark-mark {
    position: absolute; left: 125px; top: 150px;
    width: 32px; height: 32px; background: var(--emboss-blue);
  }

  .card--back .wordmark {
    position: absolute; left: 430px; top: 60px;
    color: var(--ink-white); font-size: 25px; letter-spacing: .5px;
  }
  .card--back .wordmark-mark {
    position: absolute; left: 400px; top: 65px;
    width: 18px; height: 18px; background: var(--ink-white);
  }

  .address, .contacts {
    position: absolute; left: 430px;
    font-family: "Arimo", Arial, sans-serif; color: var(--ink-white);
    font-size: 15px; line-height: 1.45; white-space: nowrap;
  }
  .address { top: 170px; }
  .contacts { top: 230px; list-style: none; }
  .contacts li { display: flex; align-items: center; gap: 8px; }
  .contacts svg { width: 13px; height: 13px; fill: var(--ink-white); flex: none; }

  .holder-tab {
    position: absolute; left: 0; top: 300px;
    width: 26px; height: 56px; background: var(--ink-white);
    border-radius: 0 6px 6px 0;
  }
  .holder {
    position: absolute; left: 54px; top: 296px; color: var(--ink-white);
  }
  .holder-name {
    font-family: "Libre Baskerville", Georgia, serif; font-weight: 700;
    font-size: 26px; text-transform: uppercase; letter-spacing: .5px;
  }
  .holder-role {
    font-family: "Arimo", Arial, sans-serif; font-size: 17px; margin-top: 4px;
  }
</style>
</head>
<body>
<main class="sheet">
  <section class="card card--front" aria-label="Card front">
    <span class="wordmark-mark"></span>
    <p class="wordmark">Brookfell<br>Construction</p>
  </section>

  <section class="card card--back" aria-label="Card back">
    <span class="wordmark-mark"></span>
    <p class="wordmark">Brookfell<br>Construction</p>

    <p class="address">P.O. Box&nbsp; Street Name<br>Country Name AB, A5B 521</p>

    <ul class="contacts">
      <li><svg viewBox="0 0 16 16"><path d="M3 1h3l1.5 4-2 1.5a9 9 0 0 0 4 4L11 8.5l4 1.5v3a2 2 0 0 1-2 2A12 12 0 0 1 1 3a2 2 0 0 1 2-2z"/></svg>555 014 2287</li>
      <li><svg viewBox="0 0 16 16"><path d="M1 3h14v10H1z M1 3l7 6 7-6" fill="none" stroke="#fff" stroke-width="1.6"/></svg>info@brookfellconstruction.com</li>
      <li><svg viewBox="0 0 16 16"><circle cx="8" cy="8" r="6.5" fill="none" stroke="#fff" stroke-width="1.5"/><path d="M1.5 8h13M8 1.5c-3 3.5-3 9.5 0 13M8 1.5c3 3.5 3 9.5 0 13" fill="none" stroke="#fff" stroke-width="1.2"/></svg>www.brookfellconstruction.com</li>
    </ul>

    <span class="holder-tab"></span>
    <div class="holder">
      <p class="holder-name">Daniel Renwick</p>
      <p class="holder-role">Owner &amp; Manager</p>
    </div>
  </section>
</main>
</body>
</html>
```